Canadian furniture distributor

I need a logo design for my new company, Pellham Craft G.P., Ergonomic High-End furniture distribution (very attractive patented design -mainly Desks & Chairs-).

Can be used for children adults, elders or limited mobility people.

Colors and design should match logo colors and products.

Industry/Entity Type

It Company

```html
<!DOCTYPE html>
<html lang="en">
<head>
<meta charset="utf-8">
<title>Pellham Craft – Business Card</title>
<link rel="stylesheet" href="https://fonts.googleapis.com/css2?family=Open+Sans:wght@700&display=swap">
<style>
  :root {
    --stage: #000000;
    --paper: #ffffff;
    --plum: #8e2150;
    --gold: #f5b21a;
    --frame-yellow: #f7e600;
    --desk-pink: #f6c9dc;
    --desk-pink-light: #fdeef4;
  }
  * { box-sizing: border-box; margin: 0; padding: 0; }
  html, body {
    width: 1200px; height: 1000px; overflow: hidden;
    background: var(--stage);
    font-family: "Open Sans", Arial, sans-serif;
    font-weight: 700;
  }
  .canvas { position: relative; width: 1200px; height: 1000px; }

  .card { position: absolute; left: 258px; width: 682px; background: var(--paper); }

  /* Front */
  .card-front { top: 97px; height: 390px; }
  .front-panel {
    position: absolute; left: 14px; top: 14px; width: 656px; height: 363px;
    background: var(--plum);
    border: 3px solid var(--frame-yellow);
    display: flex; align-items: center; justify-content: center; gap: 16px;
  }
  .brand-mark { width: 30px; height: 30px; background: var(--gold); }
  .brand-name-front { color: var(--paper); font-size: 48px; letter-spacing: -0.5px; }

  /* Back */
  .card-back { top: 521px; height: 389px; }
  .product-visual {
    position: absolute; left: 26px; top: 28px; width: 412px; height: 340px;
    background: radial-gradient(ellipse at 50% 45%, var(--desk-pink) 0%, var(--desk-pink-light) 65%, var(--paper) 100%);
  }
  .brand-name-back {
    position: absolute; left: 50px; top: 126px;
    color: var(--plum); font-size: 38px; letter-spacing: -0.5px;
  }
  .person { position: absolute; right: 29px; top: 58px; text-align: right; }
  .person-name { color: var(--plum); font-size: 28px; line-height: 1.1; }
  .person-role { color: var(--gold); font-size: 14px; letter-spacing: 0.5px; }

  .contacts {
    position: absolute; right: 28px; top: 245px;
    list-style: none; text-align: right;
  }
  .contacts li {
    color: var(--plum); font-size: 15.5px; line-height: 22.5px;
    display: flex; justify-content: flex-end; align-items: center; gap: 6px;
  }
  .contacts svg { width: 16px; height: 16px; flex: none; }

  .address {
    position: absolute; right: 29px; top: 325px;
    color: var(--plum); font-size: 15.5px; line-height: 21px;
    text-align: right; font-style: normal;
  }
</style>
</head>
<body>
<main class="canvas">
  <section class="card card-front">
    <div class="front-panel">
      <span class="brand-mark"></span>
      <span class="brand-name-front">Pellham Craft</span>
    </div>
  </section>

  <section class="card card-back">
    <div class="product-visual" role="img" aria-label="Faded pink height-adjustable ergonomic desk"></div>
    <div class="brand-name-back">Pellham Craft</div>

    <div class="person">
      <p class="person-name">Alex Moreau</p>
      <p class="person-role">DIRECTOR</p>
    </div>

    <ul class="contacts">
      <li>(555) 014-2290
        <svg viewBox="0 0 16 16" aria-hidden="true"><path fill="var(--gold)" d="M2 6c0-2 2-3 6-3s6 1 6 3l-1 1.5-2.5-.8V5.5H5.5v1.2L3 7.5zM4.5 8h7l1.5 5H3z"/><circle cx="8" cy="10.5" r="1.4" fill="#fff"/></svg>
      </li>
      <li>info@pellhamcraft.com
        <svg viewBox="0 0 16 16" aria-hidden="true"><rect x="1" y="3.5" width="14" height="9" fill="var(--gold)"/><path d="M1.5 4l6.5 5 6.5-5M1.5 12l4.5-4M14.5 12l-4.5-4" stroke="#fff" stroke-width="1" fill="none"/></svg>
      </li>
      <li>www.pellhamcraft.com
        <svg viewBox="0 0 16 16" aria-hidden="true"><circle cx="8" cy="8" r="7" fill="var(--gold)"/><g stroke="#fff" stroke-width="0.9" fill="none"><ellipse cx="8" cy="8" rx="3" ry="7"/><path d="M1 8h14M2 4.5h12M2 11.5h12M8 1v14"/></g></svg>
      </li>
    </ul>

    <address class="address">
      118 Larkspur Avenue, NW<br>
      Suite H&nbsp; Ottawa, ON K1P 0B4
    </address>
  </section>
</main>
</body>
</html>
```